Healthy Food Healthy Brain Rack Card

We want a new 2 page (front and page) 3.67" x 8.5" rack card. This rack card is the first of a series we are creating. We will have five more eventually.

The minimum font size for the text on the front is 11 point and also for other main body text.

Use the text on the word document.

The images and layout in the word document are just sample ideas we had.

We have a subscripton to pelvane stock images so prefer to get images from there or free high quality images.

The document is for older readers. Do not put text over graphics and keep it simple and easy to read with high contrast.

We are open to any color scheme, though something that conveys fresh and healthy, is good.

We want some very simple design element(s) incorporated that convey Native American communities or heritage. But NO head dress, teepee graphics, etc.

At the top, of the first page we would like a collage of healthy food images. This can include fish, chicken, fresh vegetables, berries, brown rice, etc.

On the back side, the text below the brown box on the word document with the title "mock up" can be smaller as needed.

Please remember to include the funding statement - it can be in a very small font 6/7 point.

For more information about our project, please visit https://morvetlin.org/brain-health/

```html
<!DOCTYPE html>
<html lang="en">
<head>
<meta charset="utf-8">
<title>Healthy Food Healthy Brain – Rack Card</title>
<link href="https://fonts.googleapis.com/css2?family=Montserrat:wght@400;600;700;800&family=Roboto:wght@400;500;700&display=swap" rel="stylesheet">
<style>
  :root {
    --backdrop: #b7b98c;
    --leaf-green: #6b9a44;
    --deep-maroon: #6e2a22;
    --cream: #f4f3d6;
    --paper: #ffffff;
    --ink: #262626;
    --on-dark: #ffffff;
    --accent-teal: #2aa3b5;
  }
  * { box-sizing: border-box; margin: 0; padding: 0; }
  html, body {
    width: 1200px; height: 900px; overflow: hidden;
    background: var(--backdrop);
    font-family: "Roboto", Arial, sans-serif;
    color: var(--ink);
  }
  .rack-card {
    position: absolute; top: 40px;
    width: 354px; height: 820px;
    display: flex; flex-direction: column;
    overflow: hidden;
    box-shadow: 0 6px 18px rgba(60, 60, 30, 0.25);
  }
  .rack-card--front { left: 216px; background: var(--cream); }
  .rack-card--back { left: 630px; background: var(--paper); }

  /* Front */
  .top-stripe { height: 10px; background: var(--leaf-green); }
  .food-collage {
    height: 140px;
    background: linear-gradient(100deg, #c9824a 0%, #4a3b5e 30%, #6b6f8a 45%, #e8e4d8 60%, #5f8a3c 70%, #d9682a 85%, #e07a35 100%);
  }
  .front-body { padding: 18px 24px 0 26px; flex: 1; }
  .title-small {
    font-family: "Montserrat", Arial, sans-serif;
    font-weight: 400; font-size: 23px; line-height: 1.1;
  }
  .title-large {
    font-family: "Montserrat", Arial, sans-serif;
    font-weight: 800; font-size: 34px; line-height: 1.05;
    margin-bottom: 10px;
  }
  .intro { font-size: 13px; line-height: 1.32; margin-bottom: 10px; }
  .steps-heading {
    font-family: "Montserrat", Arial, sans-serif;
    color: var(--leaf-green); font-weight: 700; font-size: 14.5px;
    margin-bottom: 6px;
  }
  .steps-list { list-style: none; }
  .steps-list li {
    position: relative; padding-left: 16px;
    font-size: 13px; line-height: 1.3; margin-bottom: 4px;
  }
  .steps-list li::before {
    content: ""; position: absolute; left: 2px; top: 6px;
    width: 6px; height: 6px; border-radius: 50%;
    background: var(--leaf-green);
  }
  .front-closing {
    border-top: 6px solid var(--leaf-green);
    background: var(--deep-maroon); color: var(--on-dark);
    text-align: center; padding: 18px 20px 22px;
    font-size: 13.5px; line-height: 1.35;
  }
  .front-closing p + p { margin-top: 10px; }
  .quote-source { font-weight: 700; display: block; }
  .tagline { font-family: "Montserrat", Arial, sans-serif; font-weight: 700; font-size: 14.5px; }

  /* Back */
  .recipe-header {
    background: var(--leaf-green); color: var(--on-dark);
    text-align: center; padding: 12px 10px 10px;
  }
  .recipe-title { font-family: "Montserrat", Arial, sans-serif; font-weight: 700; font-size: 20px; }
  .recipe-subtitle { font-family: "Montserrat", Arial, sans-serif; font-weight: 600; font-size: 13px; margin-top: 2px; }
  .recipe-photo {
    height: 120px;
    background: linear-gradient(100deg, #e6c23a 0%, #c97a4a 30%, #8a4a30 55%, #d89a6a 75%, #f0d25a 100%);
  }
  .ingredients-tab {
    align-self: center; margin-top: -14px;
    background: var(--deep-maroon); color: var(--on-dark);
    font-family: "Montserrat", Arial, sans-serif; font-weight: 600;
    font-size: 13px; letter-spacing: 3px;
    padding: 5px 22px; border-radius: 10px;
  }
  .recipe-body { padding: 10px 22px 0 24px; }
  .ingredients { display: flex; gap: 12px; margin-bottom: 10px; }
  .ingredients ul { list-style: none; flex: 1; }
  .ingredients li {
    position: relative; padding-left: 11px;
    font-size: 12.5px; line-height: 1.3;
  }
  .ingredients li::before {
    content: ""; position: absolute; left: 0; top: 6px;
    width: 5px; height: 5px; border-radius: 50%; background: var(--leaf-green);
  }
  .ingredients strong { font-weight: 700; }
  .method { font-size: 12.5px; line-height: 1.3; text-align: justify; }
  .careful {
    color: var(--leaf-green); font-family: "Montserrat", Arial, sans-serif;
    font-weight: 700; font-size: 15px; text-align: center; margin: 6px 0 10px;
  }
  .community-note {
    background: var(--deep-maroon); color: var(--on-dark);
    text-align: center; font-weight: 500;
    font-size: 12.5px; line-height: 1.3; padding: 12px 20px;
  }
  .resources {
    flex: 1; background: var(--cream);
    padding: 14px 22px 12px 24px; position: relative;
    display: flex; flex-direction: column;
  }
  .resource { font-size: 12px; line-height: 1.3; margin-bottom: 7px; padding-right: 86px; }
  .resource strong { font-family: "Montserrat", Arial, sans-serif; font-weight: 700; font-size: 12px; }
  .resource.wide { padding-right: 0; }
  .partner-mark {
    position: absolute; right: 18px; top: 16px;
    display: flex; flex-direction: column; align-items: center; gap: 4px;
    width: 76px; text-align: center;
    font-family: "Roboto", Arial, sans-serif; font-weight: 700;
    font-size: 10px; line-height: 1.15; color: var(--accent-teal);
  }
  .partner-mark .mark-dot {
    width: 30px; height: 30px; border-radius: 50%; background: var(--accent-teal);
  }
  .funding {
    margin-top: auto; font-size: 7px; line-height: 1.3; color: var(--ink);
  }
</style>
</head>
<body>

<article class="rack-card rack-card--front">
  <div class="top-stripe"></div>
  <div class="food-collage" role="img" aria-label="Collage of healthy foods: almonds, grapes, cauliflower and carrots"></div>
  <div class="front-body">
    <h1>
      <span class="title-small" style="display:block">Healthy Food</span>
      <span class="title-large" style="display:block">Healthy Brain</span>
    </h1>
    <p class="intro">Everyone slows down as they get older, both in body and mind. Eating healthier food can help your overall health, including brain health. It may also reduce your risk for memory loss and problems thinking.</p>
    <h2 class="steps-heading">Healthier steps to protect your brain:</h2>
    <ul class="steps-list">
      <li>Eat more vegetables, fruits, whole grains, and lower-fat milk</li>
      <li>Use less salt and added sugar</li>
      <li>Eat more fish, chicken, turkey, beans, and nuts</li>
      <li>Cut down on bad fats (“saturated” and trans), cholesterol, and red meat</li>
      <li>Buy fresh, not packaged food when you can</li>
      <li>Limit how much alcohol you drink</li>
      <li>Learn your daily calorie needs for your body size</li>
      <li>Take care of your mental and spiritual health to support your physical and brain health</li>
    </ul>
  </div>
  <footer class="front-closing">
    <p>Talk to your doctor about more steps to healthier food choices.</p>
    <p>“Without the elk, salmon, huckleberries, shellfish, and cedar trees we are nobody...” <span class="quote-source">Lena Tahlo (Riverbend)</span></p>
    <p class="tagline">Small changes can make a big difference for better brain health.</p>
  </footer>
</article>

<article class="rack-card rack-card--back">
  <header class="recipe-header">
    <h2 class="recipe-title">Make This at Home</h2>
    <p class="recipe-subtitle">Grilled Salmon and Veggie Foil Packets</p>
  </header>
  <div class="recipe-photo" role="img" aria-label="Grilled salmon fillet with lemon and vegetables"></div>
  <div class="ingredients-tab">INGREDIENTS:</div>
  <div class="recipe-body">
    <div class="ingredients">
      <ul>
        <li>Salmon</li>
        <li>Asparagus</li>
        <li>Red or Green Peppers <strong>(Or any seasonal vegetable)</strong></li>
        <li>Onion</li>
      </ul>
      <ul>
        <li>Lemon – sliced</li>
        <li>Basil</li>
        <li>Olive Oil</li>
        <li>Salt and Pepper</li>
        <li>Garlic Powder</li>
      </ul>
    </div>
    <p class="method">Cut asparagus, peppers, and onion into bite-size pieces. Cut salmon into 4-6 oz pieces. Tear tin foil large enough to wrap around salmon &amp; veggies (2 layers). Add veggies and salmon to foil. Drizzle with olive oil, season with salt, pepper, basil, garlic &amp; top with a piece of sliced lemon. Wrap foil tightly around food. Grill at 400 degrees for about 20 minutes.</p>
    <p class="careful">Careful opening!</p>
  </div>
  <p class="community-note">Food &amp; drink are a source of strength and connection to community. A return to traditional food pathways and eating local, seasonal fresh foods make healthier eating easier.</p>
  <section class="resources">
    <div class="partner-mark">
      <span class="mark-dot"></span>
      <span>Kinmind Resource Center</span>
    </div>
    <p class="resource"><strong>For More Information About Healthier Eating FillYourPlate</strong><br>https://www.fillyourplate.org</p>
    <p class="resource"><strong>About Brain Health</strong><br>Kinmind Resource Center for Native Brain Health<br>https://www.kinmindhealth.org</p>
    <p class="resource wide"><strong>NHA Memory Health Program</strong><br>https://www.nha-health.org/aging</p>
    <p class="funding">This product is supported by the Northfield Health Agency (NHA) of the Department of Wellness Services (DWS) as part of a financial assistance award totaling $348,711 with 100 percent funded by NHA/DWS. The contents are those of the author(s) and do not necessarily represent the official views of, nor an endorsement, by NHA/DWS, or the government.</p>
  </section>
</article>

</body>
</html>
```